Letterhead & Business Card for our Professional Practice (Financial Services)

We are looking for someone to design a letterhead and business card for our business, which is a professional practice called Harbor Lumen Capital Limited. The website is at www.harborrlumencapital.example.co.uk.

The letterhead needs to have: (a) our logo (b) address (c) telephone number (d) email address and (e) our company number.

We would like the stationary to be consistent with the website.

I have attached the logo in EPS and PNG format.

Target Market(s)

Professional services, large commercial enterprises, financial services

Industry/Entity Type

Financial Service

Font styles to use
Serif

Colors
3176b5
f04a50

Requirements
Must have
• Be consistent with our website located at www.harborlumencapital.example.co.uk
• Be in the following formats:
• 1. Word template for the letterhead
• 2. PDF for the letterhead with setup and bleeds required at www.presskite.example.co.uk
• 3. PDF for the business card with setup and bleeds required at www.presskite.example.co.uk
Nice to have
• Something with a really interesting design that says "these guys are professional but dynamic and interesting"
Should not have
• Boring

```html
<!DOCTYPE html>
<html lang="en">
<head>
<meta charset="utf-8">
<title>Harbor Lumen Capital – Business Card</title>
<link rel="stylesheet" href="https://fonts.googleapis.com/css2?family=Arimo:wght@400;700&display=swap">
<style>
  :root {
    --navy: #0f4784;
    --navy-deep: #0b3a6e;
    --red: #d9232e;
    --white: #ffffff;
    --ink: #1d3f73;
    --backdrop: #2b2b2d;
  }
  * { margin: 0; padding: 0; box-sizing: border-box; }
  html, body {
    width: 1200px;
    height: 950px;
    overflow: hidden;
    background: var(--backdrop);
    font-family: "Arimo", Arial, sans-serif;
  }
  .canvas {
    position: relative;
    width: 1200px;
    height: 950px;
  }
  .card {
    position: absolute;
    width: 620px;
    height: 354px;
    overflow: hidden;
    box-shadow: 0 18px 40px rgba(0,0,0,0.55);
  }

  /* Card back */
  .card-back {
    left: 80px;
    top: 90px;
    background: linear-gradient(160deg, #16528f 0%, var(--navy) 55%, var(--navy-deep) 100%);
  }
  .card-back .brand {
    position: absolute;
    top: 118px;
    left: 0;
    right: 0;
    display: flex;
    justify-content: center;
    align-items: center;
    gap: 14px;
  }
  .card-back .brand-square {
    width: 34px;
    height: 34px;
    background: var(--white);
  }
  .card-back .brand-name {
    color: var(--white);
    font-weight: 700;
    font-size: 30px;
    letter-spacing: 0.5px;
  }
  .card-back .website {
    position: absolute;
    bottom: 60px;
    left: 0;
    right: 0;
    text-align: center;
    color: var(--white);
    font-size: 15px;
    letter-spacing: 3px;
  }

  /* Card front */
  .card-front {
    left: 500px;
    top: 500px;
    background: var(--white);
  }
  .card-front .wave {
    position: absolute;
    inset: 0;
  }
  .card-front .brand {
    position: absolute;
    top: 44px;
    right: 40px;
    display: flex;
    align-items: center;
    gap: 10px;
  }
  .card-front .brand-square {
    width: 22px;
    height: 22px;
    background: var(--red);
  }
  .card-front .brand-name {
    color: var(--ink);
    font-weight: 700;
    font-size: 24px;
  }
  .holder {
    position: absolute;
    top: 140px;
    right: 44px;
    text-align: right;
    color: var(--white);
  }
  .holder-name { font-weight: 700; font-size: 17px; }
  .holder-role { font-size: 13px; margin-top: 3px; }

  .contact {
    position: absolute;
    left: 36px;
    bottom: 26px;
    color: var(--white);
    font-size: 13px;
    line-height: 1.35;
  }
  .address { margin-bottom: 10px; }
  .contact-list { list-style: none; }
  .contact-list li {
    display: flex;
    align-items: center;
    gap: 10px;
    margin-top: 4px;
  }
  .contact-list svg { width: 14px; height: 14px; flex: none; }
</style>
</head>
<body>
<main class="canvas">

  <section class="card card-back" aria-label="Business card back">
    <div class="brand">
      <span class="brand-square"></span>
      <span class="brand-name">Harbor Lumen Capital</span>
    </div>
    <p class="website">www.harborrlumencapital.example.co.uk</p>
  </section>

  <section class="card card-front" aria-label="Business card front">
    <svg class="wave" viewBox="0 0 620 354" preserveAspectRatio="none" aria-hidden="true">
      <path d="M0,192 C170,222 330,140 620,96 L620,354 L0,354 Z" fill="#0f4784"/>
      <path d="M0,181 C170,211 330,129 620,85" fill="none" stroke="#d9232e" stroke-width="2.5"/>
    </svg>

    <div class="brand">
      <span class="brand-square"></span>
      <span class="brand-name">Harbor Lumen Capital</span>
    </div>

    <div class="holder">
      <p class="holder-name">Martin Ellery</p>
      <p class="holder-role">President</p>
    </div>

    <div class="contact">
      <p class="address">4127 Kestrel Avenue<br>Brookhaven, NY 11719</p>
      <ul class="contact-list">
        <li>
          <svg viewBox="0 0 14 14" aria-hidden="true"><path d="M3 1.5 L5.5 1.5 L6.3 4.5 L4.8 5.6 C5.6 7.3 6.7 8.4 8.4 9.2 L9.5 7.7 L12.5 8.5 L12.5 11 C12.5 11.8 11.8 12.5 11 12.5 C5.8 12.2 1.8 8.2 1.5 3 C1.5 2.2 2.2 1.5 3 1.5 Z" fill="#fff"/></svg>
          <span>555 0147 2286</span>
        </li>
        <li>
          <svg viewBox="0 0 14 14" aria-hidden="true"><rect x="1" y="3" width="12" height="8.5" fill="#fff"/><path d="M1 3 L7 8 L13 3" fill="none" stroke="#0f4784" stroke-width="1.2"/></svg>
          <span>martin@example.com</span>
        </li>
        <li>
          <svg viewBox="0 0 14 14" aria-hidden="true"><circle cx="7" cy="7" r="6" fill="#fff"/><path d="M1 7 H13 M7 1 C4.5 4 4.5 10 7 13 M7 1 C9.5 4 9.5 10 7 13" fill="none" stroke="#0f4784" stroke-width="1"/></svg>
          <span>harborrlumencapital.example.co.uk</span>
        </li>
      </ul>
    </div>
  </section>

</main>
</body>
</html>
```